Patient Engagement Solution

We need an attractive and easy-to-use GUI for patients and clinicians, which includes screens and icons. The application has been named Quorvix. I have our corporate logo attached as well.
I have attached the screens that the developer has used to create the solution, but we all know they miss the target when it comes to the creative stuff.
If it helps, I can supply some competitor's screens as a guide - please let me know.

Target Market(s)

Patients and Clinicians

Industry/Entity Type

Healthcare/Hospitals

Font styles to use
Other font styles liked:
• Easy to Read

Requirements
Must have
• Attractive, easy to use graphical user interface. Screen size is usually 22" 16:9
Nice to have
• Inviting and interesting look
Should not have
• Complicated hard to navigate screens

```html
<!DOCTYPE html>
<html lang="en">
<head>
<meta charset="utf-8">
<title>Quorvix – Patient Engagement Screens</title>
<link rel="stylesheet" href="https://fonts.googleapis.com/css2?family=Poppins:wght@400;500;600;700&display=swap">
<style>
  :root {
    --paper: #ededec;
    --ink: #0d0d0d;
    --label-grey: #6e6e6e;
    --accent-red: #e3192b;
    --icon-red: #e0262f;
    --icon-dark-red: #a3141c;
    --icon-white: #f3f4f7;
    --icon-grey: #c3c8d4;
    --icon-yellow: #f6c343;
    --icon-green: #3fa24f;
    --icon-blue: #2f6fe0;
    --screen-edge: #34385a;
    --screen-blue: #1c4f80;
    --screen-navy: #0b1140;
    --screen-plum: #3b1433;
    --tile-fill: rgba(255, 255, 255, 0.045);
    --tile-line: rgba(255, 255, 255, 0.09);
    --tile-text: #b7bccd;
    --white: #ffffff;
  }
  * { box-sizing: border-box; margin: 0; padding: 0; }
  html, body { width: 1200px; height: 2170px; overflow: hidden; }
  body { background: var(--paper); font-family: "Poppins", sans-serif; position: relative; }

  .board-brand {
    position: absolute; top: 140px; left: 0; width: 1200px;
    display: flex; justify-content: center; align-items: center; gap: 22px;
  }
  .board-brand .brand-dot { width: 26px; height: 26px; border-radius: 50%; background: var(--accent-red); }
  .board-brand .brand-name { font-size: 60px; font-weight: 700; color: var(--ink); letter-spacing: -1.5px; line-height: 1; }

  .section-label {
    position: absolute; left: 171px;
    transform: translate(-50%, -50%) rotate(-90deg);
    font-size: 29px; font-weight: 700; color: var(--label-grey);
    white-space: nowrap; letter-spacing: 0.3px;
  }
  .label-home { top: 501px; }
  .label-services { top: 1089px; }
  .label-language { top: 1676px; }

  .screen {
    position: absolute; left: 264px; width: 773px; height: 430px;
    border-radius: 22px; border: 4px solid var(--screen-edge); overflow: hidden;
    background:
      radial-gradient(ellipse 55% 45% at 85% 100%, rgba(120, 24, 70, 0.55), transparent 70%),
      radial-gradient(ellipse 60% 55% at 10% 5%, rgba(40, 100, 160, 0.55), transparent 70%),
      linear-gradient(135deg, var(--screen-blue) 0%, var(--screen-navy) 45%, #0d0f35 70%, var(--screen-plum) 100%);
  }
  .screen-home { top: 287px; }
  .screen-services { top: 870px; }
  .screen-language { top: 1462px; }

  .screen-brand {
    position: absolute; top: 110px; left: 0; width: 100%;
    display: flex; justify-content: center; align-items: center; gap: 9px;
  }
  .screen-brand .brand-dot { width: 9px; height: 9px; border-radius: 50%; background: var(--accent-red); }
  .screen-brand .brand-name { font-size: 19px; font-weight: 600; color: var(--white); line-height: 1; }

  .tile-row { position: absolute; display: flex; gap: 21.6px; }
  .tile {
    width: 66px; height: 70px; border-radius: 13px;
    background: var(--tile-fill); border: 1px solid var(--tile-line);
    display: flex; flex-direction: column; align-items: center; padding-top: 11px;
  }
  .tile.is-focused { border-bottom: 2px solid var(--accent-red); }
  .tile-icon { width: 36px; height: 34px; display: block; }
  .tile-flag { width: 46px; height: 33px; border-radius: 3px; margin-top: -1px; }
  .tile-label { margin-top: 5px; font-size: 7.5px; color: var(--tile-text); line-height: 1; white-space: nowrap; }

  .home-row { top: 190px; left: 135px; }
  .services-row-top { top: 158px; left: 91px; }
  .services-row-bottom { top: 258px; left: 47px; }
  .language-row-top { top: 159px; left: 178px; }
  .language-row-bottom { top: 251px; left: 178px; }

  .status-bar {
    position: absolute; top: 390px; left: 0; width: 100%; padding-right: 135px;
    display: flex; justify-content: center; align-items: center; gap: 14px;
    color: rgba(255, 255, 255, 0.28); font-size: 8px;
  }
  .status-bar .status-time { font-size: 19px; color: rgba(255, 255, 255, 0.35); }
  .status-bar .status-divider { width: 1px; height: 14px; background: rgba(255, 255, 255, 0.18); }

  .home-button {
    position: absolute; left: 735px; top: 391px; width: 20px; height: 20px;
    border-radius: 50%; background: rgba(255, 255, 255, 0.12);
    display: flex; align-items: center; justify-content: center;
  }

  .closing-note {
    position: absolute; top: 2026px; left: 0; width: 1200px; text-align: center;
    font-size: 32px; font-weight: 700; color: var(--ink);
  }
</style>
</head>
<body>

<header class="board-brand">
  <span class="brand-dot"></span>
  <span class="brand-name">Quorvix</span>
</header>

<div class="section-label label-home">01.HOME SCREEN</div>
<div class="section-label label-services">02.SERVICES SCREEN</div>
<div class="section-label label-language">03.LANGUAGE SCREEN</div>

<!-- Home screen -->
<section class="screen screen-home">
  <div class="screen-brand"><span class="brand-dot"></span><span class="brand-name">Quorvix</span></div>
  <div class="tile-row home-row">
    <div class="tile">
      <svg class="tile-icon" viewBox="0 0 32 32" aria-label="Start">
        <circle cx="16" cy="16" r="12" fill="var(--icon-red)"/>
        <path d="M13 10 L22 16 L13 22 Z" fill="var(--icon-white)"/>
      </svg>
      <span class="tile-label">Start</span>
    </div>
    <div class="tile">
      <svg class="tile-icon" viewBox="0 0 32 32" aria-label="Television">
        <path d="M12 4 L16 8 L20 4" stroke="var(--icon-grey)" stroke-width="1.5" fill="none"/>
        <rect x="3" y="8" width="26" height="18" rx="3" fill="var(--icon-red)"/>
        <rect x="6" y="11" width="15" height="12" rx="1.5" fill="var(--icon-white)"/>
        <rect x="8" y="11" width="3" height="12" fill="var(--icon-yellow)"/>
        <rect x="14" y="11" width="3" height="12" fill="var(--icon-blue)"/>
        <circle cx="25" cy="14" r="1.6" fill="var(--icon-white)"/>
        <circle cx="25" cy="19" r="1.6" fill="var(--icon-white)"/>
      </svg>
      <span class="tile-label">TV</span>
    </div>
    <div class="tile is-focused">
      <svg class="tile-icon" viewBox="0 0 32 32" aria-label="Radio">
        <path d="M8 10 L26 4" stroke="var(--icon-grey)" stroke-width="1.5"/>
        <rect x="3" y="10" width="26" height="17" rx="3" fill="var(--icon-red)"/>
        <rect x="6" y="14" width="11" height="1.6" fill="var(--icon-white)"/>
        <rect x="6" y="18" width="11" height="1.6" fill="var(--icon-white)"/>
        <rect x="6" y="22" width="11" height="1.6" fill="var(--icon-white)"/>
        <circle cx="23" cy="19" r="4" fill="var(--icon-white)"/>
        <circle cx="23" cy="19" r="1.6" fill="var(--icon-dark-red)"/>
      </svg>
      <span class="tile-label">Radio</span>
    </div>
    <div class="tile">
      <svg class="tile-icon" viewBox="0 0 32 32" aria-label="Apps">
        <rect x="4" y="4" width="11" height="11" rx="3" fill="var(--icon-red)"/>
        <rect x="17" y="4" width="11" height="11" rx="3" fill="var(--icon-yellow)"/>
        <rect x="4" y="17" width="11" height="11" rx="3" fill="var(--icon-green)"/>
        <rect x="17" y="17" width="11" height="11" rx="3" fill="var(--icon-blue)"/>
      </svg>
      <span class="tile-label">Apps</span>
    </div>
    <div class="tile">
      <svg class="tile-icon" viewBox="0 0 32 32" aria-label="Language">
        <rect x="3" y="3" width="16" height="16" rx="3" fill="var(--icon-red)"/>
        <text x="11" y="15.5" text-anchor="middle" font-family="Poppins, sans-serif" font-size="12" font-weight="700" fill="var(--icon-white)">A</text>
        <rect x="13" y="13" width="16" height="16" rx="3" fill="var(--icon-white)"/>
        <path d="M16.5 17.5 H25.5 M21 16 V18 M17.5 26 C21 24 23 21 23.5 17.5 M19 21 C20.5 23.5 23 25.5 25.5 26" stroke="var(--icon-red)" stroke-width="1.5" fill="none" stroke-linecap="round"/>
      </svg>
      <span class="tile-label">Language</span>
    </div>
    <div class="tile">
      <svg class="tile-icon" viewBox="0 0 32 32" aria-label="Clock">
        <circle cx="16" cy="17" r="12" fill="var(--icon-red)"/>
        <circle cx="16" cy="17" r="8.5" fill="var(--icon-white)"/>
        <path d="M16 12 V17 L19.5 19" stroke="#1a1a1a" stroke-width="1.8" fill="none" stroke-linecap="round"/>
      </svg>
      <span class="tile-label">Clock</span>
    </div>
  </div>
  <div class="status-bar">
    <span>Demo Ward</span><span class="status-divider"></span>
    <span class="status-time">15.35</span><span class="status-divider"></span>
    <span>Default bed</span>
  </div>
</section>

<!-- Services screen -->
<section class="screen screen-services">
  <div class="screen-brand"><span class="brand-dot"></span><span class="brand-name">Quorvix</span></div>
  <div class="tile-row services-row-top">
    <div class="tile">
      <svg class="tile-icon" viewBox="0 0 32 32" aria-label="Video call">
        <rect x="3" y="9" width="18" height="14" rx="3" fill="var(--icon-red)"/>
        <path d="M21 14 L29 9.5 V22.5 L21 18 Z" fill="var(--icon-dark-red)"/>
        <path d="M10 13 L15 16 L10 19 Z" fill="var(--icon-white)"/>
      </svg>
      <span class="tile-label">Video Call</span>
    </div>
    <div class="tile">
      <svg class="tile-icon" viewBox="0 0 32 32" aria-label="Relax">
        <path d="M4 20 H10 L4 28 H10" stroke="var(--icon-grey)" stroke-width="2" fill="none" stroke-linejoin="round"/>
        <path d="M12 12 H19 L12 21 H19" stroke="var(--icon-red)" stroke-width="2.2" fill="none" stroke-linejoin="round"/>
        <path d="M20 3 H28 L20 13 H28" stroke="var(--icon-red)" stroke-width="2.4" fill="none" stroke-linejoin="round"/>
      </svg>
      <span class="tile-label">Relax</span>
    </div>
    <div class="tile">
      <svg class="tile-icon" viewBox="0 0 32 32" aria-label="Internet">
        <circle cx="16" cy="16" r="12" fill="var(--icon-red)" stroke="var(--icon-white)" stroke-width="1.5"/>
        <ellipse cx="16" cy="16" rx="5" ry="12" fill="none" stroke="var(--icon-white)" stroke-width="1.3"/>
        <path d="M4 16 H28 M6 10 H26 M6 22 H26" stroke="var(--icon-white)" stroke-width="1.3"/>
      </svg>
      <span class="tile-label">Internet</span>
    </div>
    <div class="tile is-focused">
      <svg class="tile-icon" viewBox="0 0 32 32" aria-label="Clinical">
        <rect x="5" y="11" width="22" height="18" fill="var(--icon-white)"/>
        <rect x="11" y="4" width="10" height="10" rx="2" fill="var(--icon-red)"/>
        <path d="M16 6 V12 M13 9 H19" stroke="var(--icon-white)" stroke-width="1.8"/>
        <rect x="8" y="16" width="3" height="3" fill="var(--icon-red)"/>
        <rect x="14.5" y="16" width="3" height="3" fill="var(--icon-red)"/>
        <rect x="21" y="16" width="3" height="3" fill="var(--icon-red)"/>
        <rect x="13.5" y="22" width="5" height="7" fill="var(--icon-dark-red)"/>
      </svg>
      <span class="tile-label">Clinical</span>
    </div>
    <div class="tile">
      <svg class="tile-icon" viewBox="0 0 32 32" aria-label="Education">
        <path d="M2 12 L16 6 L30 12 L16 18 Z" fill="var(--icon-red)"/>
        <path d="M8 15 V22 C8 25 24 25 24 22 V15 L16 18.5 Z" fill="var(--icon-dark-red)"/>
        <path d="M27 13 V21" stroke="var(--icon-yellow)" stroke-width="1.5"/>
        <circle cx="27" cy="22" r="1.6" fill="var(--icon-yellow)"/>
      </svg>
      <span class="tile-label">Education</span>
    </div>
    <div class="tile">
      <svg class="tile-icon" viewBox="0 0 32 32" aria-label="Meals">
        <circle cx="16" cy="16" r="11" fill="var(--icon-white)"/>
        <circle cx="16" cy="16" r="7" fill="none" stroke="var(--icon-grey)" stroke-width="1.2"/>
        <path d="M2.5 6 V12 M4.5 6 V12 M3.5 12 V27" stroke="var(--icon-red)" stroke-width="1.4" stroke-linecap="round"/>
        <path d="M29 6 C27 9 27 13 29 15 V27" stroke="var(--icon-red)" stroke-width="1.6" fill="none" stroke-linecap="round"/>
      </svg>
      <span class="tile-label">Meals</span>
    </div>
    <div class="tile">
      <svg class="tile-icon" viewBox="0 0 32 32" aria-label="Books">
        <rect x="4" y="5" width="5" height="22" rx="1" fill="var(--icon-red)"/>
        <rect x="10" y="8" width="5" height="19" rx="1" fill="var(--icon-blue)"/>
        <rect x="16" y="20" width="13" height="3.5" rx="1" fill="var(--icon-green)"/>
        <rect x="16" y="23.5" width="13" height="3.5" rx="1" fill="var(--icon-white)"/>
        <circle cx="22.5" cy="15" r="4" fill="var(--icon-red)"/>
      </svg>
      <span class="tile-label">Books</span>
    </div>
  </div>
  <div class="tile-row services-row-bottom">
    <div class="tile">
      <svg class="tile-icon" viewBox="0 0 32 32" aria-label="Settings">
        <circle cx="13" cy="13" r="7" fill="none" stroke="var(--icon-grey)" stroke-width="4" stroke-dasharray="3 2.5"/>
        <circle cx="13" cy="13" r="5" fill="var(--icon-grey)"/>
        <circle cx="13" cy="13" r="2" fill="var(--screen-navy)"/>
        <circle cx="22" cy="22" r="5.5" fill="none" stroke="var(--icon-red)" stroke-width="3.5" stroke-dasharray="2.5 2"/>
        <circle cx="22" cy="22" r="4" fill="var(--icon-red)"/>
        <circle cx="22" cy="22" r="1.5" fill="var(--icon-white)"/>
      </svg>
      <span class="tile-label">Settings</span>
    </div>
    <div class="tile">
      <svg class="tile-icon" viewBox="0 0 32 32" aria-label="Apps">
        <rect x="4" y="4" width="11" height="11" rx="3" fill="var(--icon-red)"/>
        <rect x="17" y="4" width="11" height="11" rx="3" fill="var(--icon-yellow)"/>
        <rect x="4" y="17" width="11" height="11" rx="3" fill="var(--icon-green)"/>
        <rect x="17" y="17" width="11" height="11" rx="3" fill="var(--icon-blue)"/>
      </svg>
      <span class="tile-label">Apps</span>
    </div>
    <div class="tile">
      <svg class="tile-icon" viewBox="0 0 32 32" aria-label="Concierge bell">
        <circle cx="16" cy="7" r="2" fill="var(--icon-red)"/>
        <path d="M5 23 C5 15 10 10 16 10 C22 10 27 15 27 23 Z" fill="var(--icon-red)"/>
        <path d="M10 19 C10.5 16 12.5 14 15 13.5" stroke="var(--icon-white)" stroke-width="1.4" fill="none" stroke-linecap="round"/>
        <rect x="3" y="24" width="26" height="3.5" rx="1.5" fill="var(--icon-grey)"/>
      </svg>
      <span class="tile-label">Concierge</span>
    </div>
    <div class="tile">
      <svg class="tile-icon" viewBox="0 0 32 32" aria-label="Phone">
        <path d="M3 12 C3 6 29 6 29 12 L26 15 L21 13 V10 C18 9 14 9 11 10 V13 L6 15 Z" fill="var(--icon-grey)"/>
        <path d="M8 16 L11 13 H21 L24 16 V27 H8 Z" fill="var(--icon-red)"/>
        <circle cx="16" cy="21" r="4" fill="var(--icon-white)"/>
        <circle cx="16" cy="21" r="1.5" fill="var(--icon-red)"/>
      </svg>
      <span class="tile-label">Phone</span>
    </div>
    <div class="tile">
      <svg class="tile-icon" viewBox="0 0 32 32" aria-label="Code scanner">
        <path d="M4 10 V4 H10 M22 4 H28 V10 M28 22 V28 H22 M10 28 H4 V22" stroke="var(--icon-grey)" stroke-width="2" fill="none"/>
        <path d="M7 16 H25" stroke="var(--icon-red)" stroke-width="2.2" stroke-linecap="round"/>
        <circle cx="16" cy="16" r="3.5" fill="none" stroke="var(--icon-red)" stroke-width="1.6"/>
      </svg>
      <span class="tile-label">Bar Code</span>
    </div>
    <div class="tile">
      <svg class="tile-icon" viewBox="0 0 32 32" aria-label="Games">
        <path d="M8 9 H24 C28 9 30 15 30 21 C30 25 27 26 25 23 L22 19 H10 L7 23 C5 26 2 25 2 21 C2 15 4 9 8 9 Z" fill="var(--icon-white)"/>
        <path d="M9 13 V18 M6.5 15.5 H11.5" stroke="var(--icon-red)" stroke-width="1.8"/>
        <circle cx="22" cy="13.5" r="1.5" fill="var(--icon-red)"/>
        <circle cx="25" cy="16.5" r="1.5" fill="var(--icon-blue)"/>
      </svg>
      <span class="tile-label">Games</span>
    </div>
    <div class="tile">
      <svg class="tile-icon" viewBox="0 0 32 32" aria-label="My care">
        <path d="M16 22 C8 16 6 12 8 9 C10 6 14 7 16 10 C18 7 22 6 24 9 C26 12 24 16 16 22 Z" fill="var(--icon-red)"/>
        <path d="M3 18 C5 22 9 26 14 27 M29 18 C27 22 23 26 18 27" stroke="var(--icon-white)" stroke-width="2.4" fill="none" stroke-linecap="round"/>
      </svg>
      <span class="tile-label">My Care</span>
    </div>
    <div class="tile">
      <svg class="tile-icon" viewBox="0 0 32 32" aria-label="Movies">
        <path d="M4 9 L26 4 L27 8 L5 13 Z" fill="var(--icon-white)"/>
        <path d="M9 8 L11 11 M15 6.5 L17 9.5 M21 5 L23 8" stroke="#1a1a1a" stroke-width="1.4"/>
        <rect x="4" y="14" width="24" height="14" rx="2" fill="var(--icon-red)"/>
        <path d="M8 19 H20 M8 23 H16" stroke="var(--icon-white)" stroke-width="1.6" stroke-linecap="round"/>
      </svg>
      <span class="tile-label">Movies</span>
    </div>
  </div>
  <div class="home-button">
    <svg width="10" height="10" viewBox="0 0 10 10"><path d="M1 5 L5 1.5 L9 5 V9 H1 Z" fill="#d6d8e0"/></svg>
  </div>
</section>

<!-- Language screen -->
<section class="screen screen-language">
  <div class="screen-brand"><span class="brand-dot"></span><span class="brand-name">Quorvix</span></div>
  <div class="tile-row language-row-top">
    <div class="tile">
      <svg class="tile-flag" viewBox="0 0 46 33" aria-label="United Kingdom flag">
        <rect width="46" height="33" fill="#1f3f8f"/>
        <path d="M0 0 L46 33 M46 0 L0 33" stroke="#ffffff" stroke-width="6"/>
        <path d="M0 0 L46 33 M46 0 L0 33" stroke="#d9262e" stroke-width="2"/>
        <path d="M23 0 V33 M0 16.5 H46" stroke="#ffffff" stroke-width="9"/>
        <path d="M23 0 V33 M0 16.5 H46" stroke="#d9262e" stroke-width="5"/>
      </svg>
      <span class="tile-label">Video Call</span>
    </div>
    <div class="tile"><div class="tile-flag" role="img" aria-label="French flag" style="background:linear-gradient(90deg,#2b3f8f 33%,#ffffff 33% 66%,#e2323c 66%)"></div><span class="tile-label">French</span></div>
    <div class="tile is-focused"><div class="tile-flag" role="img" aria-label="Japanese flag" style="background:radial-gradient(circle,#e2323c 30%,#f4f4f4 32%)"></div><span class="tile-label">Japanese</span></div>
    <div class="tile"><div class="tile-flag" role="img" aria-label="Italian flag" style="background:linear-gradient(90deg,#2e9a4a 33%,#ffffff 33% 66%,#e2323c 66%)"></div><span class="tile-label">Italian</span></div>
    <div class="tile"><div class="tile-flag" role="img" aria-label="Spanish flag" style="background:linear-gradient(180deg,#d9262e 25%,#f7c623 25% 75%,#d9262e 75%)"></div><span class="tile-label">Spanish</span></div>
  </div>
  <div class="tile-row language-row-bottom">
    <div class="tile"><div class="tile-flag" role="img" aria-label="Chinese flag" style="background:radial-gradient(circle at 25% 30%,#f6d23a 10%,#e2323c 14%)"></div><span class="tile-label">Chinese</span></div>
    <div class="tile"><div class="tile-flag" role="img" aria-label="German flag" style="background:linear-gradient(180deg,#1a1a1a 33%,#dd2a2f 33% 66%,#f7c623 66%)"></div><span class="tile-label">German</span></div>
    <div class="tile">
      <svg class="tile-flag" viewBox="0 0 46 33" aria-label="Indian flag">
        <rect width="46" height="11" fill="#f39a2b"/>
        <rect y="11" width="46" height="11" fill="#ffffff"/>
        <rect y="22" width="46" height="11" fill="#2f9a46"/>
        <circle cx="23" cy="16.5" r="4" fill="none" stroke="#23308f" stroke-width="1"/>
        <circle cx="23" cy="16.5" r="1" fill="#23308f"/>
      </svg>
      <span class="tile-label">Hindi</span>
    </div>
    <div class="tile">
      <svg class="tile-flag" viewBox="0 0 46 33" aria-label="Vietnamese flag">
        <rect width="46" height="33" fill="#e2323c"/>
        <path d="M23 8 L25.2 14.2 L31.6 14.3 L26.5 18.2 L28.4 24.5 L23 20.7 L17.6 24.5 L19.5 18.2 L14.4 14.3 L20.8 14.2 Z" fill="#f7d63a"/>
      </svg>
      <span class="tile-label">Vietnamese</span>
    </div>
    <div class="tile"><div class="tile-flag" role="img" aria-label="United Arab Emirates flag" style="background:linear-gradient(90deg,#e2323c 25%,transparent 25%),linear-gradient(180deg,#2e9a4a 33%,#ffffff 33% 66%,#111111 66%)"></div><span class="tile-label">Arabic</span></div>
  </div>
  <div class="home-button">
    <svg width="10" height="10" viewBox="0 0 10 10"><path d="M1 5 L5 1.5 L9 5 V9 H1 Z" fill="#d6d8e0"/></svg>
  </div>
</section>

<p class="closing-note">Thanks for Watching My Works</p>

</body>
</html>
```